Interior designer needs business card design

I need a card for my new interior design company. I de sign mostly kitchens and baths, but don't want the card to list and specialty. I've gotten several clients already by Dordrecht of mouth, but now need to begin advertising.
I've got a pic of a silk screen used to print my father's old real estate sign and was hoping to use it as the basis for my card design.
Instead of "Sold by Marivone", I'd like the front of my card to read "Design by Marivone".
I like the font styles and banner and would like to stay as close to the original as possible, but with some twist--maybe color, not sure. Surprise me!
The back should list my email and phone
marivonedesign@quillpost.example
225-555-0193

```html
<!DOCTYPE html>
<html lang="en">
<head>
<meta charset="utf-8">
<title>Marivone Design – Business Card</title>
<link rel="stylesheet" href="https://fonts.googleapis.com/css2?family=Anton&family=Arimo:ital,wght@1,700&display=swap">
<style>
  :root {
    --page: #ffffff;
    --card: #000000;
    --ink: #ffffff;
    --banner-fill: #1c1c1c;
    --shadow: rgba(0, 0, 0, 0.45);
  }
  * { margin: 0; padding: 0; box-sizing: border-box; }
  html, body {
    width: 1000px;
    height: 1200px;
    overflow: hidden;
    background: var(--page);
  }
  .canvas {
    position: relative;
    width: 1000px;
    height: 1200px;
  }
  .card {
    position: absolute;
    width: 746px;
    height: 532px;
    background: var(--card);
    box-shadow: 10px 12px 18px var(--shadow);
    color: var(--ink);
  }
  .card--front { left: 34px; top: 34px; }
  .card--back  { left: 198px; top: 616px; }

  .tagline {
    position: absolute;
    z-index: 2;
    font-family: "Anton", "Oswald", sans-serif;
    font-size: 54px;
    line-height: 1;
    letter-spacing: 3px;
    text-transform: uppercase;
  }
  .tagline--designed { left: 156px; top: 106px; }
  .tagline--by { left: 238px; top: 168px; }

  .banner-area {
    position: absolute;
    z-index: 1;
    left: 106px;
    top: 232px;
    width: 534px;
    height: 190px;
    background: var(--banner-fill);
    border-radius: 18px;
  }
  .brand-name {
    position: absolute;
    z-index: 2;
    left: 106px;
    top: 270px;
    width: 534px;
    text-align: center;
    font-family: "Anton", "Oswald", sans-serif;
    font-size: 96px;
    line-height: 1.2;
    letter-spacing: 3px;
    text-transform: uppercase;
    color: var(--ink);
  }

  .contact {
    position: absolute;
    left: 38px;
    top: 406px;
    font-family: "Arimo", Arial, sans-serif;
    font-style: italic;
    font-weight: 700;
    font-size: 32px;
    line-height: 44px;
    white-space: nowrap;
  }
</style>
</head>
<body>
<main class="canvas">
  <section class="card card--front" aria-label="Card front">
    <p class="tagline tagline--designed">Designed</p>
    <p class="tagline tagline--by">By</p>
    <div class="banner-area" role="img" aria-label="Unfurled scroll banner ornament framing the company name"></div>
    <h1 class="brand-name">Marivone</h1>
  </section>

  <section class="card card--back" aria-label="Card back">
    <div class="contact">
      <p class="contact__email">Email: marivonedesign@quillpost.example</p>
      <p class="contact__phone">Tel: 225-555-0193</p>
    </div>
  </section>
</main>
</body>
</html>
```